Trade Show Booth

We need a Single booth design size and below are the requirements from the event holder.
How to provide graphics:
Single booth: Graphic size is 1993 mm width x 2483 mm height
Naming file: Name the files as Company name_ size_scale_bleed, for example: “Tour Brova_1993x2483mm_scale1_10_ bleed50mm.”
Bleed & Marks: 50mm bleed all around, no marks, and no crop marks.
Resolution: Please try to keep graphics over 100 dpi to maintain good quality.

We are a DMC in Iceland and will be participating in a Travel show.
www.brightfjordtrips.example

We would like to work with someone who could help us create this and potentially some marketing material for the show.

```html
<!DOCTYPE html>
<html lang="en">
<head>
<meta charset="utf-8">
<title>Tour Brova – Single Booth Graphic</title>
<link rel="stylesheet" href="https://fonts.googleapis.com/css2?family=Poppins:wght@500;700&family=Barlow+Condensed:wght@400;500&family=Kaushan+Script&display=swap">
<style>
  :root{
    --stage:#e4e5e8;
    --white:#ffffff;
    --navy:#1a2170;
    --navy-deep:#141a5c;
    --royal:#2a4fb0;
    --sky:#3f86d4;
    --ice:#6e9fe0;
    --tick:#4a9be0;
  }
  *{margin:0;padding:0;box-sizing:border-box}
  html,body{width:1200px;height:722px;overflow:hidden;background:var(--stage)}
  .canvas{position:relative;width:1200px;height:722px}
  .booth-graphic{
    position:absolute;left:313px;top:16px;
    width:855px;height:1030px;
    transform:scale(0.67);transform-origin:top left;
    background:var(--white);overflow:hidden;
    box-shadow:0 6px 20px rgba(0,0,0,.15);
  }
  .booth-shapes{position:absolute;inset:0}
  .brand-name{
    position:absolute;left:0;right:0;top:92px;text-align:center;
    font-family:"Poppins",sans-serif;font-weight:700;font-size:84px;
    letter-spacing:1px;color:var(--navy);line-height:1;
  }
  .headline{
    position:absolute;left:40px;width:370px;top:725px;text-align:center;
    font-family:"Poppins",sans-serif;font-weight:700;text-transform:uppercase;
    color:var(--white);font-size:52px;line-height:48px;
  }
  .headline .accent{color:var(--ice)}
  .headline .script{
    display:block;text-transform:none;font-family:"Kaushan Script",cursive;
    font-weight:400;font-size:78px;line-height:90px;margin-top:4px;
  }
  .divider{
    position:absolute;left:418px;top:745px;width:2px;height:190px;
    background:rgba(255,255,255,.7);
  }
  .service-list{
    position:absolute;left:462px;top:728px;list-style:none;
    font-family:"Barlow Condensed",sans-serif;font-weight:400;
    font-size:22px;line-height:25px;color:var(--white);text-transform:uppercase;
  }
  .service-list li{display:flex;align-items:center;gap:10px}
  .service-list svg{width:17px;height:17px;flex:none}
  .contact{
    position:absolute;left:462px;top:906px;
    font-family:"Poppins",sans-serif;font-weight:700;color:var(--white);
    font-size:26px;line-height:32px;
  }
  .contact div{display:flex;align-items:center;gap:8px}
  .contact svg{width:18px;height:18px;flex:none}
</style>
</head>
<body>
<div class="canvas">
  <div class="booth-graphic">
    <svg class="booth-shapes" viewBox="0 0 855 1030" width="855" height="1030">
      <defs>
        <linearGradient id="photoGroup" x1="0" y1="0" x2="0" y2="1">
          <stop offset="0" stop-color="#7c8a5a"/><stop offset=".5" stop-color="#a4503a"/><stop offset="1" stop-color="#3a4f78"/>
        </linearGradient>
        <linearGradient id="photoLagoon" x1="0" y1="0" x2="0" y2="1">
          <stop offset="0" stop-color="#4fa6e0"/><stop offset=".6" stop-color="#b9d9ea"/><stop offset="1" stop-color="#6aa7cf"/>
        </linearGradient>
        <linearGradient id="photoCave" x1="0" y1="0" x2="0" y2="1">
          <stop offset="0" stop-color="#121216"/><stop offset=".5" stop-color="#3d6fa8"/><stop offset="1" stop-color="#2b3142"/>
        </linearGradient>
        <linearGradient id="footerFill" x1="0" y1="0" x2="1" y2="0">
          <stop offset="0" stop-color="var(--navy-deep)"/><stop offset=".45" stop-color="var(--royal)"/><stop offset="1" stop-color="var(--navy)"/>
        </linearGradient>
      </defs>

      <polygon role="img" aria-label="Photo: group of hikers by a river in autumn woodland" fill="url(#photoGroup)" points="0,170 292,170 232,760 0,760"/>
      <polygon role="img" aria-label="Photo: tour boat among icebergs on a glacier lagoon" fill="url(#photoLagoon)" points="300,170 628,170 568,760 240,760"/>
      <polygon role="img" aria-label="Photo: climber with rope at the mouth of an ice cave" fill="url(#photoCave)" points="636,170 855,170 855,760 576,760"/>

      <path d="M0,190 Q428,420 855,175" fill="none" stroke="var(--sky)" stroke-width="18"/>
      <path d="M0,182 Q428,405 855,170" fill="none" stroke="var(--navy)" stroke-width="12"/>
      <path d="M0,0 H855 V175 Q428,395 0,175 Z" fill="var(--white)"/>

      <path d="M0,700 Q428,560 855,720 V1030 H0 Z" fill="var(--sky)"/>
      <path d="M0,750 Q428,590 855,740 V1030 H0 Z" fill="url(#footerFill)"/>
    </svg>

    <div class="brand-name">TOUR BROVA</div>

    <h1 class="headline">Plan your<br>ultimate<br><span class="accent">Iceland</span><span class="script">Vacation!</span></h1>

    <div class="divider"></div>

    <ul class="service-list">
      <li><svg viewBox="0 0 16 16"><circle cx="8" cy="8" r="8" fill="var(--tick)"/><path d="M4.5 8.2l2.3 2.3 4.7-4.8" stroke="#fff" stroke-width="2" fill="none"/></svg>Tour Brova Tours</li>
      <li><svg viewBox="0 0 16 16"><circle cx="8" cy="8" r="8" fill="var(--tick)"/><path d="M4.5 8.2l2.3 2.3 4.7-4.8" stroke="#fff" stroke-width="2" fill="none"/></svg>Iceland Tours</li>
      <li><svg viewBox="0 0 16 16"><circle cx="8" cy="8" r="8" fill="var(--tick)"/><path d="M4.5 8.2l2.3 2.3 4.7-4.8" stroke="#fff" stroke-width="2" fill="none"/></svg>Private Day Tours</li>
      <li><svg viewBox="0 0 16 16"><circle cx="8" cy="8" r="8" fill="var(--tick)"/><path d="M4.5 8.2l2.3 2.3 4.7-4.8" stroke="#fff" stroke-width="2" fill="none"/></svg>Custom Tours</li>
      <li><svg viewBox="0 0 16 16"><circle cx="8" cy="8" r="8" fill="var(--tick)"/><path d="M4.5 8.2l2.3 2.3 4.7-4.8" stroke="#fff" stroke-width="2" fill="none"/></svg>Incentive Trips and Conferences</li>
      <li><svg viewBox="0 0 16 16"><circle cx="8" cy="8" r="8" fill="var(--tick)"/><path d="M4.5 8.2l2.3 2.3 4.7-4.8" stroke="#fff" stroke-width="2" fill="none"/></svg>Things to do in Reykjavik</li>
    </ul>

    <div class="contact">
      <div><svg viewBox="0 0 16 16"><path d="M3 1.5l3 .5 1 3-2 1.5a9 9 0 0 0 4.5 4.5L11 9l3 1 .5 3-2 1.5C7 14 2 9 1.5 3.5z" fill="var(--ice)"/></svg>00354 555 0199</div>
      <div><svg viewBox="0 0 16 16" fill="none" stroke="var(--ice)" stroke-width="1.3"><circle cx="8" cy="8" r="6.5"/><ellipse cx="8" cy="8" rx="3" ry="6.5"/><path d="M1.5 8h13M2.5 4.8h11M2.5 11.2h11"/></svg>brightfjordtrips.example</div>
    </div>
  </div>
</div>
</body>
</html>
```